Uncoded website + logo for game server company

We're looking to refresh our website - plinthware.net. We are a server provider that specializes in Tilecraft servers, as well as voice servers. Our primary goal is to keep the same essential layout but get a more modern, updated, and smooth look; our current site is a bit cluttered and unprofessional, and doesn't lend too well to ease of use.

Our color scheme is blue and white, though the shade of blue can vary. We are happy to experiment with other colors as well, but blue is recognized as our main color. The shades in use on our current site are a good starting point.

We would like the design to be flat and modern, sleek, and clean. Since we provide services relating to Tilecraft, some sort of integration with Tilecraft themes would be preferable; eg. elements from the game. The design should not be overly professional as we serve primary a young demographic, but it should still convey a sense of professionalism in that our network and infrastructure is solid.

For our logo, we would like a geometric/cube-based design. We would like to see "PlinthWare" used within the logo, rather than "7Ware" as it is now. A flat design would be preferred with single or two-tone color scheme using blue/black/white and perhaps other small accent colors. An icon/symbol integrated with the logo would suit us very well.

We would love to keep in contact with the winning designer and continue work on both our current website and other websites in the future.
Please email marcel@plinthware.net with any additional questions.

** Colors listed are examples that we like, not required **
** No HTML/CSS/JS is required to be submitted; we only need the design. ***

Feel free to submit a single page design for review and we will determine if a full design is necessary. If you choose to do this, please use the home page and/or the Tilecraft page.
Updates

Target Market(s)

Our target demographic is comprised of young (14 - 24 y/o) gamers and community owners. Because of the audience, the design should be easy to follow and not overly complicated; should be straightforward with its features and options.

Industry/Entity Type

It Company

Font styles to use
Sans Serif

Colors
3276b5
0092cd
ceddec
cde9f5
ecf7fa
ffffff
85abd2

Requirements
Must have
• Required pages:
- Home page with main features and news/updates
- Tilecraft page with features and customization options
- Tilecraft VPS page, similar to Tilecraft page
- Voice servers page with features and customization options
- Dedicated servers page with package listings and features + customization options
- Stub page for other basic pages (ToS/AUP/Careers)

Product pages (Tilecraft/voice/dedicated):
- Product overview area with area for summary
- Features area for overview of all included features (such as on current site - see Tilecraft)
- Customization options (eg. value sliders) with price display and list of features
Nice to have
• A slider on the front page would be nice, based on HTML elements rather than images as we do not have a graphic designer (utilizing text and background color/texture elements vs fully designed images).
An area for testimonials/quotes from customers
Social icons

```html
<!DOCTYPE html>
<html lang="en">
<head>
<meta charset="utf-8">
<title>PlinthWare – Game Server Hosting</title>
<link rel="stylesheet" href="https://fonts.googleapis.com/css2?family=Source+Sans+3:ital,wght@0,300;0,400;0,600;1,400&display=swap">
<style>
:root{
  --brand:#3276b5;
  --accent:#0092cd;
  --link:#1f6fb8;
  --ink:#333;
  --muted:#555;
  --line:#d5d5d5;
  --quote-bg:#efefef;
  --footer:#111;
  --white:#fff;
  --fb:#3b5ba8;
  --tw:#2b9ad9;
  --rss:#f47a20;
  --yt:#d9252a;
}
*{box-sizing:border-box;margin:0;padding:0}
html,body{width:960px;height:1200px;overflow:hidden;background:var(--white)}
body{font-family:"Source Sans 3",sans-serif;color:var(--ink);position:relative}
a{color:inherit;text-decoration:none}

.topbar{position:absolute;left:0;top:0;width:960px;height:38px;background:var(--brand);color:var(--white);font-size:13px}
.topbar .greeting{position:absolute;left:71px;top:11px}
.topbar nav{position:absolute;right:72px;top:11px;display:flex;gap:34px;font-weight:600;letter-spacing:.2px}

.header{position:absolute;left:0;top:38px;width:960px;height:122px}
.brand{position:absolute;left:69px;top:44px;display:flex;align-items:center;gap:8px;font-size:24px;font-weight:600;color:var(--brand)}
.brand .mark{width:22px;height:22px;background:var(--accent)}
.search{position:absolute;left:682px;top:24px;width:208px;height:29px;border:1px solid #ccc;font-size:13px;color:#777;padding:6px 10px}
.search svg{position:absolute;right:8px;top:7px}
.mainnav{position:absolute;right:69px;top:80px;display:flex;gap:33px;font-size:15px;color:#444}

.hero{position:absolute;left:0;top:160px;width:960px;height:338px;background:linear-gradient(90deg,#b9bcc0 0%,#d8d6d2 35%,#c9c7c2 65%,#a8a49a 100%)}
.hero h1{position:absolute;left:88px;top:76px;font-weight:300;font-size:29px;line-height:42px;color:var(--white);letter-spacing:.3px}
.hero h2{position:absolute;left:88px;top:173px;font-weight:400;font-size:26px;color:var(--brand)}
.hero p{position:absolute;left:88px;top:216px;font-size:14px;color:var(--brand)}
.hero .devices{position:absolute;left:540px;top:28px;width:282px;height:270px;background:linear-gradient(135deg,#2b2b2b,#6d7278 60%,#d9dde2);border-radius:14px}
.dots{position:absolute;right:72px;top:314px;display:flex;gap:3px}
.dots span{width:8px;height:8px;border-radius:50%;background:#333;border:1px solid #333}
.dots span:first-child{background:var(--white)}

.features{position:absolute;left:48px;top:530px;width:864px;display:flex}
.feature{width:216px;text-align:center}
.feature svg{display:block;margin:0 auto;height:56px}
.feature h3{font-size:19px;font-weight:400;color:var(--brand);margin-top:10px}
.feature p{font-size:12px;line-height:17px;color:var(--muted);margin:6px auto 0;width:185px;letter-spacing:.2px}

.section-title{position:absolute;font-size:19px;font-weight:400;color:#222}
.welcome-photo{position:absolute;left:70px;top:775px;width:210px;height:132px;background:radial-gradient(circle at 55% 55%,#d8821e 0%,#6e4a22 25%,#182533 60%,#0d1620 100%)}
.welcome-text{position:absolute;left:302px;top:771px;width:322px;font-size:12.5px;line-height:20px;color:#666}

.news{position:absolute;left:663px;top:771px;width:230px;list-style:none}
.news li{position:relative;padding-left:18px;margin-bottom:17px}
.news li::before{content:"";position:absolute;left:0;top:4px;width:10px;height:10px;border-radius:50%;background:#888}
.news li::after{content:"";position:absolute;left:4px;top:7px;border-left:3px solid #fff;border-top:2px solid transparent;border-bottom:2px solid transparent}
.news h4{font-size:13px;font-weight:400;color:var(--link)}
.news p{font-size:12.5px;line-height:20px;color:#444;margin-top:4px}

.testimonials{position:absolute;left:66px;top:971px;width:825px;display:flex;justify-content:space-between}
.testimonial{width:262px;position:relative}
.testimonial blockquote{background:var(--quote-bg);padding:11px 16px 11px 17px;font-style:italic;font-size:11px;line-height:19px;color:#555;height:78px;position:relative}
.testimonial blockquote::before{content:"\201C";position:absolute;left:3px;top:-2px;font-size:22px;color:#bbb;font-style:normal}
.testimonial blockquote::after{content:"";position:absolute;left:185px;bottom:-14px;border-top:14px solid var(--quote-bg);border-right:20px solid transparent}
.testimonial cite{display:flex;align-items:center;gap:8px;font-style:normal;font-size:11.5px;font-weight:600;color:#333;margin:22px 0 0 151px}

.footer{position:absolute;left:0;top:1116px;width:960px;height:84px;background:var(--footer);color:var(--white);font-size:11px}
.footer .links{position:absolute;left:69px;top:28px}
.footer .copy{position:absolute;left:69px;top:55px}
.social{position:absolute;right:69px;top:27px;display:flex;gap:11px}
.social span{width:29px;height:29px;display:block}
.social .fb{background:var(--fb)}
.social .tw{background:var(--tw)}
.social .rss{background:var(--rss)}
.social .yt{background:var(--yt)}
</style>
</head>
<body>

<div class="topbar">
  <span class="greeting">Welcome, guest!</span>
  <nav><a href="#">MANAGE</a><a href="#">BLOG</a><a href="#">STATUS</a><a href="#">SUPPORT</a></nav>
</div>

<header class="header">
  <a class="brand" href="#"><span class="mark"></span>PlinthWare</a>
  <div class="search">Search..
    <svg width="12" height="12" viewBox="0 0 12 12"><circle cx="5" cy="5" r="3.8" fill="none" stroke="#999" stroke-width="1.6"/><line x1="8" y1="8" x2="11" y2="11" stroke="#999" stroke-width="1.8"/></svg>
  </div>
  <nav class="mainnav"><a href="#">HOME</a><a href="#">TILECRAFT VOICE</a><a href="#">WEB</a><a href="#">DEDICATED</a><a href="#">FAQ</a></nav>
</header>

<section class="hero" role="img" aria-label="Blurred office background">
  <h1>MANAGE YOUR SERVERS<br>ANYWHERE IN THE WORLD</h1>
  <h2>Official PlinthWare LumoOS App</h2>
  <p>Coming soon to Lumo Phone and Lumo Tab</p>
  <div class="devices" role="img" aria-label="Tablet and phone showing the PlinthWare site"></div>
  <div class="dots"><span></span><span></span><span></span><span></span></div>
</section>

<section class="features">
  <div class="feature">
    <svg viewBox="0 0 56 56" width="56" fill="none" stroke="var(--accent)" stroke-width="5">
      <line x1="8" y1="2" x2="8" y2="54"/><line x1="28" y1="2" x2="28" y2="54"/><line x1="48" y1="2" x2="48" y2="54"/>
      <rect x="3" y="14" width="10" height="9" fill="#fff" stroke-width="3"/><rect x="23" y="34" width="10" height="9" fill="#fff" stroke-width="3"/><rect x="43" y="14" width="10" height="9" fill="#fff" stroke-width="3"/>
    </svg>
    <h3>Instant Setup</h3>
    <p>Lorem ipsum dolor sit ametadipis msan. Morbi ut elit utipsa Pellent esque habitant morbi.</p>
  </div>
  <div class="feature">
    <svg viewBox="0 0 66 56" width="66" fill="var(--accent)">
      <circle cx="20" cy="30" r="14"/><circle cx="36" cy="22" r="17"/><circle cx="52" cy="32" r="12"/><rect x="14" y="30" width="40" height="14"/>
      <path d="M33 20 L45 33 H38 V50 H28 V33 H21 Z" fill="#fff"/><path d="M33 24 L41 32 H36 V48 H30 V32 H25 Z" fill="var(--accent)"/>
    </svg>
    <h3>Automatic Backups</h3>
    <p>Lorem ipsum dolor sit ametadipis msan. Morbi ut elit utipsa Pellent esque habitant morbi.</p>
  </div>
  <div class="feature">
    <svg viewBox="0 0 66 56" width="66">
      <path d="M28 3 C13 3 3 12 3 23 C3 31 8 37 14 40 L10 52 L24 43 C25 43 27 43 28 43" fill="none" stroke="var(--accent)" stroke-width="6"/>
      <path d="M28 3 C43 3 52 11 53 22" fill="none" stroke="var(--accent)" stroke-width="6"/>
      <circle cx="45" cy="36" r="16" fill="var(--accent)"/><path d="M50 48 L60 55 L57 44 Z" fill="var(--accent)"/>
    </svg>
    <h3>Awesome Support</h3>
    <p>Lorem ipsum dolor sit ametadipis msan. Morbi ut elit utipsa Pellent esque habitant morbi.</p>
  </div>
  <div class="feature">
    <svg viewBox="0 0 66 56" width="66">
      <path d="M8 4 H58 L62 32 H4 Z" fill="var(--accent)"/>
      <rect x="3" y="35" width="60" height="14" rx="3" fill="var(--accent)"/>
      <circle cx="55" cy="42" r="2" fill="#fff"/>
    </svg>
    <h3>Powerful Hardware</h3>
    <p>Lorem ipsum dolor sit ametadipis msan. Morbi ut elit utipsa Pellent esque habitant morbi.</p>
  </div>
</section>

<h2 class="section-title" style="left:69px;top:728px">Welcome</h2>
<div class="welcome-photo" role="img" aria-label="Hand touching a glowing interface of device icons"></div>
<p class="welcome-text">Duis autem vel eum iriure dolor in hendrerit in vulputate velit esse moilestie consequat, vel illum dolore eu feugiat nulla facl isis at vero eros et accumsan et iusto odio dignissim qui bland it praesent luptatium zzril delenit augue duis dolore te feugait nulla facilisi. Nam liber tempor cum solutanobis eleifend optio n congue nihil imperdiet doming id quod mazim placerat face r possim assum. Typi non haibent claritatem insitam.</p>

<h2 class="section-title" style="left:665px;top:728px">Latest News</h2>
<ul class="news">
  <li><h4>Typi non habent claritatem insitam</h4><p>We are now recruiting experienced Heal th and Saftey advisors to work</p></li>
  <li><h4>Claritas est etiam processus dynamicus</h4><p>We are now recruiting experienced Heal th and Saftey advisors to work</p></li>
</ul>

<h2 class="section-title" style="left:70px;top:936px">Testimonials</h2>
<section class="testimonials">
  <figure class="testimonial">
    <blockquote>Fusce feugiat malesuada odio. Morbi nunc dograv ida at, cursus nec, luctus a, lorem. Maecnas tristiq ue orci acd sem. Lorem ipsum dolorsit amet. ”</blockquote>
    <cite><svg width="13" height="13" viewBox="0 0 13 13" fill="#555"><circle cx="6.5" cy="3.5" r="3.3"/><path d="M0 13 C0 8 3 7 6.5 7 C10 7 13 8 13 13 Z"/></svg>Ned Harlow's</cite>
  </figure>
  <figure class="testimonial">
    <blockquote>Fusce feugiat malesuada odio. Morbi nunc dograv ida at, cursus nec, luctus a, lorem. Maecnas tristiq ue orci acd sem. Lorem ipsum dolorsit amet. ”</blockquote>
    <cite><svg width="13" height="13" viewBox="0 0 13 13" fill="#555"><circle cx="6.5" cy="3.5" r="3.3"/><path d="M0 13 C0 8 3 7 6.5 7 C10 7 13 8 13 13 Z"/></svg>Sam Pryce</cite>
  </figure>
  <figure class="testimonial">
    <blockquote>Fusce feugiat malesuada odio. Morbi nunc dograv ida at, cursus nec, luctus a, lorem. Maecnas tristiq ue orci acd sem. Lorem ipsum dolorsit amet. ”</blockquote>
    <cite><svg width="13" height="13" viewBox="0 0 13 13" fill="#555"><circle cx="6.5" cy="3.5" r="3.3"/><path d="M0 13 C0 8 3 7 6.5 7 C10 7 13 8 13 13 Z"/></svg>Lena</cite>
  </figure>
</section>

<footer class="footer">
  <p class="links">Home | Tilecraft | Voice | Web | Dedicated | FAQ</p>
  <p class="copy">Copyright Brightwell/ Cornmoor, LLC 2013.&nbsp; All rights reserved.</p>
  <div class="social">
    <span class="fb" role="img" aria-label="Social network link"></span>
    <span class="tw" role="img" aria-label="Social network link"></span>
    <span class="rss" role="img" aria-label="News feed link"></span>
    <span class="yt" role="img" aria-label="Video channel link"></span>
  </div>
</footer>

</body>
</html>
```